Need to drive pregnant women to my 3d4d ultrasound studio where i provide 4d ultrasound with hyperalistic imaging and gender reveals

Industry/Entity Type

Healthcare

Font styles to use
Decorative
Script

Requirements
Must have
• My Company name Latido de Luna 4D. EVERYTHING HAS TO BE IN SPANISH
Nice to have
• SIMPLE AND NOT TOO BUSY
Should not have
• website

```html
<!DOCTYPE html>
<html lang="es">
<head>
<meta charset="utf-8">
<title>Latido de Luna 4D – Valla publicitaria</title>
<link rel="stylesheet" href="https://fonts.googleapis.com/css2?family=Anton&family=Great+Vibes&family=Poppins:wght@500;600;700&display=swap">
<style>
  :root {
    --page-bg: #d6d6d6;
    --magenta: #b23cb8;
    --violet: #8a52cc;
    --sky: #4ea3d9;
    --band: #4a0846;
    --ink: #3d0a3a;
    --pink-light: #f6bdf2;
    --white: #ffffff;
    --gold: #e0b43a;
    --gold-light: #f8e98a;
    --gender: #c21fb4;
    --reveals: #1e63c4;
    --phone-icon: #c95fd6;
  }
  html, body {
    margin: 0;
    padding: 0;
    width: 999px;
    height: 1200px;
    overflow: hidden;
    background: var(--page-bg);
  }
  .billboard {
    position: absolute;
    left: 40px;
    top: 370px;
    width: 920px;
    height: 460px;
    background: var(--white);
    box-shadow: 0 6px 14px rgba(0,0,0,0.35);
    overflow: hidden;
    font-family: "Poppins", sans-serif;
  }
  .hero-panel {
    position: absolute;
    left: 0; top: 0;
    width: 920px; height: 322px;
    background: linear-gradient(170deg, var(--magenta) 0%, var(--violet) 55%, var(--sky) 100%);
  }
  .mother-photo {
    position: absolute;
    left: 624px; top: 0;
    width: 296px; height: 322px;
    background: linear-gradient(160deg, #e7b3dc 0%, #d99ccf 55%, #c98cc2 100%);
  }
  .brand-seal {
    position: absolute;
    left: 30px; top: 33px;
    width: 118px; height: 118px;
    border-radius: 50%;
    background: var(--white);
    display: flex;
    align-items: center;
    justify-content: center;
    text-align: center;
  }
  .brand-name {
    font-weight: 600;
    font-size: 15px;
    line-height: 1.2;
    color: var(--violet);
    width: 90px;
  }
  .headline-script {
    position: absolute;
    left: 192px; top: 24px;
    margin: 0;
    font-family: "Great Vibes", cursive;
    font-weight: 400;
    font-size: 66px;
    line-height: 1;
    color: var(--white);
  }
  .headline-main {
    position: absolute;
    left: 192px; top: 96px;
    margin: 0;
    font-family: "Anton", sans-serif;
    font-weight: 400;
    font-size: 50px;
    line-height: 1;
    letter-spacing: 0.5px;
    color: var(--white);
    white-space: nowrap;
  }
  .service-band {
    position: absolute;
    left: 168px; top: 160px;
    width: 505px; height: 72px;
    background: var(--band);
    border-radius: 0 8px 8px 0;
  }
  .service-4d {
    position: absolute;
    left: 24px; top: 10px;
    font-family: "Anton", sans-serif;
    font-size: 48px;
    line-height: 1;
    color: var(--white);
  }
  .service-text {
    position: absolute;
    left: 86px; top: 10px;
    font-size: 24px;
    line-height: 26px;
    color: var(--white);
    font-weight: 500;
    white-space: nowrap;
  }
  .service-text strong {
    display: block;
    color: var(--pink-light);
    font-weight: 700;
  }
  .scan-frame {
    position: absolute;
    border: 4px solid var(--gold);
    box-sizing: border-box;
    box-shadow: 0 2px 6px rgba(0,0,0,0.35);
  }
  .scan-left {
    left: 38px; top: 154px;
    width: 137px; height: 128px;
    transform: rotate(-2deg);
    background: linear-gradient(135deg, #1a1a1a 0%, #7a3c12 40%, #c4752a 60%, #2a1408 100%);
  }
  .scan-mid {
    left: 468px; top: 240px;
    width: 100px; height: 96px;
    transform: rotate(-3deg);
    background: radial-gradient(circle at 55% 50%, #d98a3a 0%, #a3561c 55%, #3a1a08 100%);
  }
  .newborn-photo {
    left: 574px; top: 242px;
    width: 100px; height: 94px;
    transform: rotate(-3deg);
    background: linear-gradient(150deg, #f1cdbb 0%, #e6b09a 60%, #d29a86 100%);
  }
  .tagline-script {
    position: absolute;
    left: 192px; top: 246px;
    margin: 0;
    font-family: "Great Vibes", cursive;
    font-size: 29px;
    line-height: 1;
    color: var(--white);
    white-space: nowrap;
  }
  .tagline-caps {
    position: absolute;
    left: 35px; top: 288px;
    margin: 0;
    font-family: "Anton", sans-serif;
    font-size: 15px;
    letter-spacing: 0.6px;
    color: var(--white);
    font-weight: 400;
    white-space: nowrap;
  }
  .phone-icon {
    position: absolute;
    left: 36px; top: 372px;
  }
  .phone-number {
    position: absolute;
    left: 90px; top: 362px;
    font-size: 52px;
    font-weight: 700;
    line-height: 1;
    letter-spacing: -1px;
    color: var(--ink);
  }
  .follow-label {
    position: absolute;
    left: 486px; top: 378px;
    font-size: 11px;
    font-weight: 700;
    letter-spacing: 3px;
    line-height: 13px;
    color: var(--ink);
  }
  .gender-badge {
    position: absolute;
    left: 684px; top: 220px;
    width: 198px; height: 198px;
  }
  .badge-text {
    position: absolute;
    inset: 0;
    display: flex;
    flex-direction: column;
    align-items: center;
    justify-content: center;
    text-align: center;
  }
  .badge-script {
    font-family: "Great Vibes", cursive;
    font-size: 22px;
    color: var(--ink);
    line-height: 1;
    margin-bottom: 4px;
  }
  .badge-gender, .badge-reveals {
    font-family: "Anton", sans-serif;
    font-size: 31px;
    line-height: 1.05;
  }
  .badge-gender { color: var(--gender); }
  .badge-reveals { color: var(--reveals); }
</style>
</head>
<body>
  <main class="billboard">
    <div class="hero-panel"></div>
    <div class="mother-photo" role="img" aria-label="Foto de una mujer embarazada con vestido rosa sosteniendo una ecografía sobre su vientre"></div>

    <div class="brand-seal">
      <span class="brand-name">Latido de Luna 4D</span>
    </div>

    <h1 class="headline-script">Descubre el</h1>
    <h2 class="headline-main">MILAGRO DE LA VIDA</h2>

    <div class="scan-frame scan-left" role="img" aria-label="Ecografía 4D de un bebé en la pantalla de un monitor"></div>

    <div class="service-band">
      <span class="service-4d">4D</span>
      <span class="service-text">ULTRASONIDO CON<strong>IMÁGENES HIPERREALISTAS</strong></span>
    </div>

    <p class="tagline-script">Momentos Inolvidables</p>
    <p class="tagline-caps">TU CAMINO A LA MATERNIDAD, BELLAMENTE CAPTURADO</p>

    <div class="scan-frame scan-mid" role="img" aria-label="Primer plano de una ecografía 4D de un bebé"></div>
    <div class="scan-frame newborn-photo" role="img" aria-label="Foto de un bebé recién nacido dormido"></div>

    <svg class="phone-icon" width="40" height="40" viewBox="0 0 40 40" aria-hidden="true">
      <circle cx="20" cy="20" r="20" fill="var(--phone-icon)"/>
      <path d="M14 11c1-.8 2-.6 2.6.4l1.8 3c.5.8.3 1.7-.4 2.3l-1.3 1c1 2.3 2.6 4 4.8 5l1-1.3c.6-.7 1.5-.9 2.3-.4l3 1.8c1 .6 1.2 1.6.4 2.6l-1.2 1.5c-.9 1.1-2.4 1.5-3.8 1-5.4-2-9.4-6-11.4-11.4-.5-1.4-.1-2.9 1-3.8z" fill="var(--white)"/>
      <path d="M23 10.5a7 7 0 0 1 6.5 6.5M22.5 14a3.5 3.5 0 0 1 3.5 3.5" stroke="var(--white)" stroke-width="1.8" fill="none" stroke-linecap="round"/>
    </svg>
    <div class="phone-number">555-214-7390</div>

    <div class="follow-label">SÍGUENOS<br>EN</div>

    <div class="gender-badge">
      <svg width="198" height="198" viewBox="0 0 198 198" aria-hidden="true">
        <defs>
          <radialGradient id="goldFill" cx="50%" cy="45%" r="60%">
            <stop offset="0%" stop-color="var(--gold-light)"/>
            <stop offset="70%" stop-color="#f0d35c"/>
            <stop offset="100%" stop-color="var(--gold)"/>
          </radialGradient>
        </defs>
        <circle cx="99" cy="99" r="90" fill="none" stroke="var(--gold)" stroke-width="16" stroke-dasharray="12 11.56"/>
        <circle cx="99" cy="99" r="86" fill="url(#goldFill)"/>
      </svg>
      <div class="badge-text">
        <span class="badge-script">Especialistas en</span>
        <span class="badge-gender">REVELACIÓN</span>
        <span class="badge-reveals">DE GÉNERO</span>
      </div>
    </div>
  </main>
</body>
</html>
```